Signwriting for Halvorn Trekker Van

I've bought a Halvorn Trekker van for my business, and want to signwrite the sides and back. Can you help me come up with a very eyecatching design? I hope so!
Brief:
Design eye-catching signwriting for the sides and rear of a Halvorn Trekker van that will raise brand recognition for our business.
The Business:
The business is called Brightmoor Vitrines. We basically sell glass display cabinets and display cases. These are mostly used for commercial purposes (mainly retail), but also for residential. You can see what we sell on our website: www.brightmoorvitrines.example.nz.
The business is located in Auckland, New Zealand.
The Van:
The van is a 2009 Halvron Trekker, super high roof and medium wheel base. It is painted silver, so consider silver the base colour.
The van has no rear windows, so the signwriting needn't avoid any windows.
The van will be used for deliveries and other general purposes for the business, and while it is out and about I'd like it to be identifiable for where it is from and what it is doing.
The whole van is 2.6 metres tall, 1.9 metres wide and 5.75 metres long.
The Creative Brief:
The signwriting MUST:
- be very eye-catching. I don't just want a magnet on the side of the van. It must stand out from the crowd.
- be recognisable as representative of a business selling glass display cases.
- use the business logo on both sides.
- include the web address.
- consider cost as a factor in the design. I understand that great signwriting will cost money, but cost is also a factor.
The signwriting MAY:
- use other images, although it does not necessarily need to.
- use other colours beside the corporate colours of green, grey, purple and black. Remember that the van is painted silver. The CMYK colours are available upon request.
- cover the whole van, or it may cover part of it.
- be a partial or ful vehicle wrap, or it may be a vinyl print that is adhered to the van.
Glass is one of the hardest materials to represent visually. This leads me to think that an abstract design may work better, but the right photographic image could be used.
The attachments:
1. Company logo
2. A file showing some vehicle signwriting I really like. I am NOT asking you to do exactly the same thing, but I'm showing you what I think eye-catching vehicle graphics look like.
3. Photos of the van.

```html
<!DOCTYPE html>
<html lang="en">
<head>
<meta charset="utf-8">
<title>Brightmoor Vitrines – Van Signwriting</title>
<link rel="stylesheet" href="https://fonts.googleapis.com/css2?family=Jost:ital,wght@0,400;0,500;1,700&display=swap">
<style>
  :root {
    --bg: #ffffff;
    --plum: #6b3a5c;
    --steel-blue: #3e7ba7;
    --steel-blue-deep: #336b95;
    --steel-blue-shadow: #2e5f86;
    --mint: #d5e4b8;
    --white: #ffffff;
  }
  html, body {
    margin: 0;
    padding: 0;
    width: 680px;
    height: 1200px;
    overflow: hidden;
    background: var(--bg);
  }
  .canvas {
    position: relative;
    width: 680px;
    height: 1200px;
    background: var(--bg);
  }
  .van-graphic {
    position: absolute;
    left: 0;
    top: 0;
    width: 680px;
    height: 1200px;
  }
  .band-plum { fill: var(--plum); }
  .panel-blue { fill: var(--steel-blue); }
  .panel-blue-deep { fill: var(--steel-blue-deep); }
  .panel-blue-shadow { fill: var(--steel-blue-shadow); }
  .brand-square { fill: var(--mint); }
  .brand-name {
    font-family: "Jost", sans-serif;
    font-weight: 500;
    font-size: 21px;
    fill: var(--white);
    letter-spacing: 0.3px;
  }
  .brand-tagline {
    font-family: "Jost", sans-serif;
    font-weight: 400;
    font-size: 17px;
    fill: var(--white);
  }
  .web-address {
    font-family: "Jost", sans-serif;
    font-weight: 700;
    font-style: italic;
    font-size: 12.5px;
    fill: var(--white);
  }
</style>
</head>
<body>
<main class="canvas">
  <svg class="van-graphic" viewBox="0 0 680 1200" xmlns="http://www.w3.org/2000/svg">
    <!-- plum sweep: slanted stripe plus lower band -->
    <polygon class="band-plum" points="187,283 210,283 126,450 540,450 527,485 95,485"/>

    <!-- main blue panel with logo bar -->
    <polygon class="panel-blue" points="205,283 363,283 325,331 507,331 507,405 232,405 210,450 122,450"/>

    <!-- deeper blue accents -->
    <polygon class="panel-blue-shadow" points="205,283 248,283 150,420 137,420"/>
    <polygon class="panel-blue-deep" points="300,331 340,283 363,283 325,331"/>

    <!-- blue end tab on the lower band -->
    <polygon class="panel-blue" points="540,450 586,450 568,485 523,485"/>

    <!-- brand lockup -->
    <rect class="brand-square" x="192" y="354" width="32" height="32"/>
    <text class="brand-name" x="238" y="366" textLength="266" lengthAdjust="spacingAndGlyphs">BRIGHTMOOR VITRINES</text>
    <text class="brand-tagline" x="239" y="390">design strength value</text>

    <!-- web address -->
    <text class="web-address" x="330" y="472" textLength="185" lengthAdjust="spacingAndGlyphs">www.brightmoorvitrines.example.nz</text>
  </svg>
</main>
</body>
</html>
```